Business Card Design

Lintel Comms is a public relations consultancy service for the self build, home refurbishment and home improvement market.
It represents everything about 'home' so envisage logo featuring maybe roof pitch over the 'A' of Lintel. Colour/font undecided.

Industry/Entity Type

Home Improvement

Contact Information for Business Card

Fenella Coxworth
fenella@lintelcomms.co.uk
Telephone Direct: 0788 142 6597

```html
<!DOCTYPE html>
<html lang="en">
<head>
<meta charset="utf-8">
<title>Lintel Comms — Business Card</title>
<link rel="stylesheet" href="https://fonts.googleapis.com/css2?family=Michroma&display=swap">
<style>
  :root {
    --stage: #e9e9e9;
    --card: #ffffff;
    --ink: #1f1f1f;
    --ink-soft: #4a4a4a;
    --rule: #8a8a8a;
    --amber: #f7b500;
    --orange: #ee7d0c;
    --slate: #3a3a3a;
  }
  * { margin: 0; padding: 0; box-sizing: border-box; }
  html, body {
    width: 1200px; height: 735px; overflow: hidden;
    background: var(--stage);
    font-family: "Michroma", sans-serif;
    color: var(--ink);
  }
  .business-card {
    position: absolute; left: 150px; top: 110px;
    width: 900px; height: 514px;
    background: var(--card);
    overflow: hidden;
    box-shadow: 0 10px 30px rgba(0,0,0,0.12);
  }
  .accent-band {
    position: absolute; left: 0; right: 0; bottom: 0;
    height: 110px;
    background: linear-gradient(100deg, var(--amber), var(--orange));
  }

  .brand {
    position: absolute; left: 250px; top: 86px;
    display: flex; align-items: center; gap: 18px;
    white-space: nowrap;
  }
  .brand-square { width: 56px; height: 56px; background: var(--orange); flex: none; }
  .brand-name {
    font-size: 40px; letter-spacing: 1px; color: var(--ink);
    text-transform: uppercase; line-height: 1;
  }

  .details {
    position: absolute; left: 90px; top: 200px;
    display: flex; align-items: stretch;
  }
  .person {
    width: 330px; padding-right: 22px; text-align: right;
  }
  .person-name { font-size: 15px; letter-spacing: 2px; white-space: nowrap; }
  .person-role { font-size: 11px; letter-spacing: 2px; color: var(--ink-soft); margin-top: 6px; }
  .person-address { font-size: 11px; letter-spacing: 1.5px; color: var(--ink-soft); margin-top: 16px; line-height: 1.7; }
  .divider { width: 1px; background: var(--rule); }
  .contacts { list-style: none; padding-left: 22px; }
  .contacts li {
    display: flex; align-items: center; gap: 10px;
    font-size: 12px; letter-spacing: 1.5px; line-height: 22px;
    white-space: nowrap;
  }
  .contact-icon {
    width: 14px; height: 14px; border-radius: 50%;
    background: var(--slate); flex: none;
    display: flex; align-items: center; justify-content: center;
  }
  .contact-icon svg { width: 8px; height: 8px; }
</style>
</head>
<body>
  <main class="business-card">
    <div class="accent-band" role="img" aria-label="Decorative amber and orange sweeping band along the bottom of the card"></div>

    <header class="brand">
      <span class="brand-square"></span>
      <span class="brand-name">Lintel Comms</span>
    </header>

    <section class="details">
      <div class="person">
        <p class="person-name">Fenella Coxworth</p>
        <p class="person-role">Owner / C.E.O</p>
        <p class="person-address">Unit 4, Ridge House,<br>Leeds LS1 4AB</p>
      </div>
      <div class="divider"></div>
      <ul class="contacts">
        <li><span class="contact-icon"><svg viewBox="0 0 10 10"><path d="M2 1l2 2-1 1c.5 1 1.5 2 2.5 2.5l1-1 2 2-1.5 1.5C4 9 1 6 .5 2.5z" fill="#fff"/></svg></span>0788 142 6597</li>
        <li><span class="contact-icon"><svg viewBox="0 0 10 10"><rect x="3" y="1" width="4" height="8" rx="1" fill="#fff"/></svg></span>0113 496 0182</li>
        <li><span class="contact-icon"><svg viewBox="0 0 10 10"><rect x="1.5" y="3" width="7" height="5" fill="#fff"/></svg></span>0113 496 0754</li>
        <li><span class="contact-icon"><svg viewBox="0 0 10 10"><rect x="1" y="2.5" width="8" height="5" fill="#fff"/></svg></span>fenella@lintelcomms.co.uk</li>
        <li><span class="contact-icon"><svg viewBox="0 0 10 10"><circle cx="5" cy="5" r="3.5" fill="none" stroke="#fff" stroke-width="1.2"/></svg></span>www.lintelcomms.co.uk</li>
      </ul>
    </section>
  </main>
</body>
</html>
```